Website wordpress theme for brightvalecrafts.au

We need a modern dark mode website to entice customers to engage us to deliver web apps, mobile apps and VR apps. The site emphasises humans over tech.

Target Market(s)

Medium to large business and well funded startups

Industry/Entity Type

Information Technology

Coding

Coded - Design and coding required

Font styles to use
Sans Serif

Colors
EB3D1F
EC4F4E
F09395
F8D3D4
FCEDEE

Requirements
Must have
• Attractive image on home page

```html
<!DOCTYPE html>
<html lang="en">
<head>
<meta charset="utf-8">
<title>Brightvale Crafts</title>
<link href="https://fonts.googleapis.com/css2?family=Ubuntu:wght@400;500;700&family=Lato:wght@400;700&family=Poppins:wght@400;500;600&display=swap" rel="stylesheet">
<style>
:root{
  --bg:#000;
  --ink:#fff;
  --muted:#e6e6e6;
  --red:#c40000;
  --red-dark:#6e0000;
  --red-mid:#a30000;
  --card:#050505;
  --line:#9a9a9a;
}
*{box-sizing:border-box;margin:0;padding:0}
html,body{width:1200px;height:3392px;overflow:hidden;background:var(--bg);color:var(--ink);font-family:"Lato",sans-serif}
.page{position:relative;width:1200px;height:3392px}
.abs{position:absolute}
.heading{font-family:"Ubuntu",sans-serif;font-weight:500}

/* header */
.brand{left:112px;top:24px;display:flex;align-items:center;gap:12px;font-family:"Ubuntu",sans-serif;font-weight:700;font-size:30px;color:var(--ink)}
.brand-dot{width:34px;height:34px;border-radius:50%;background:var(--ink)}
.nav{left:461px;top:36px;display:flex;gap:40px;font-family:"Poppins",sans-serif;font-size:16px}
.nav a{color:var(--ink);text-decoration:none}
.nav a.active{color:var(--red)}
.pill{background:var(--ink);color:var(--red);border-radius:26px;font-family:"Ubuntu",sans-serif;font-weight:500;display:flex;align-items:center;justify-content:center;font-size:18px}
.contact-btn{left:951px;top:21px;width:137px;height:51px}

/* hero */
.hero-art{left:566px;top:100px;width:634px;height:585px;background:radial-gradient(circle at 45% 40%,#3a3d9a 0%,#5b1f8a 28%,#1a0f3a 55%,#000 80%)}
.hero-title{left:112px;top:222px;font-size:42px;line-height:53px;font-weight:700}
.hero-text{left:112px;top:346px;width:440px;font-size:14.5px;line-height:31px;color:var(--muted)}
.hero-btn{left:112px;top:419px;width:136px;height:51px}
.slider-nav{top:508px;width:27px;height:27px;border:1.5px solid #bbb;display:flex;align-items:center;justify-content:center}

/* how it works */
.section-title{width:1200px;left:0;text-align:center;font-size:34px}
.section-text{left:0;width:1200px;text-align:center;font-size:14.5px;line-height:31px;color:var(--muted)}
.step{width:230px;text-align:center}
.step-label{position:absolute;top:1050px;width:230px;text-align:center;font-family:"Ubuntu",sans-serif;font-size:22px;color:#ddd}
.step-label.active{font-weight:700;color:var(--ink)}

/* about */
.about-band{left:0;top:1170px;width:1200px;height:559px;background:radial-gradient(ellipse at 85% 45%,#143238 0%,#0a1a20 35%,#020608 75%)}
.about-photo{left:112px;top:1242px;width:454px;height:418px;border-radius:26px;background:linear-gradient(135deg,#0c2a24 0%,#0e3b30 40%,#1a5c48 60%,#07140f 100%)}
.about-title{left:599px;top:1228px;font-size:34px;font-weight:700}
.about-text{left:599px;top:1282px;width:492px;font-size:14.5px;line-height:30.8px;color:var(--muted)}
.about-btn{left:599px;top:1611px;width:136px;height:51px}

/* services */
.service{width:312px;height:435px;top:1945px;border:2px solid var(--red);border-radius:14px;background:var(--card);box-shadow:0 0 0 1px #2a0000}
.service-icon{position:absolute;left:106px;top:59px;width:100px;height:100px;border-radius:50%;background:var(--ink);display:flex;align-items:center;justify-content:center}
.service h3{position:absolute;top:198px;width:100%;text-align:center;font-family:"Ubuntu",sans-serif;font-weight:500;font-size:22px}
.service p{position:absolute;top:236px;left:18px;width:276px;text-align:center;font-size:13.5px;line-height:31px;color:var(--muted)}
.service .go{position:absolute;left:144px;top:375px}
.side-arrow{top:2155px}

/* benefits */
.benefits-band{left:0;top:2463px;width:1200px;height:447px;background:radial-gradient(ellipse at 70% 50%,#2a0f14 0%,#12070a 45%,#050305 85%)}
.benefits-title{left:108px;top:2540px;font-size:31px}
.benefits-list{left:112px;top:2598px;list-style:none;font-family:"Ubuntu",sans-serif;font-size:17.5px;color:#eee}
.benefits-list li{height:40px;display:flex;align-items:center;gap:10px}
.benefits-art{left:726px;top:2542px;width:280px;height:296px;border-radius:140px;background:linear-gradient(160deg,#5a1410 0%,#1e2c4a 45%,#3a1a24 100%)}

/* footer */
.foot-title{font-family:"Poppins",sans-serif;font-weight:500;font-size:26px;top:2964px}
.quick-links{left:112px;top:3008px;list-style:none;font-family:"Poppins",sans-serif;font-size:14.5px}
.quick-links li{height:31px;display:flex;align-items:center;gap:14px}
.socials{left:110px;top:3182px;display:flex;gap:5px}
.social{width:32px;height:32px;border:1.5px solid #ddd;border-radius:50%}
.vrule{top:2999px;width:0;height:238px;border-left:1.5px dashed #888}
.detail{left:369px;font-family:"Poppins",sans-serif}
.detail-icon{position:absolute;left:0;width:34px;height:34px;border:1.5px solid #ddd;border-radius:50%;display:flex;align-items:center;justify-content:center}
.detail-label{position:absolute;left:45px;font-size:17px;font-weight:500;white-space:nowrap}
.detail-value{position:absolute;left:45px;font-size:15px;line-height:31px;white-space:nowrap}
.dots{left:369px;width:240px;border-top:1.5px dotted #888}
.field{left:730px;width:353px;height:40px;border:1.5px solid #ccc;font-family:"Poppins",sans-serif;font-size:14px;padding:0 12px;display:flex;align-items:center;color:#eee}
.submit{left:730px;top:3171px;width:353px;height:39px;background:var(--red);font-family:"Poppins",sans-serif;font-weight:600;font-size:16px;display:flex;align-items:center;justify-content:center}
.bottom-rule{left:99px;top:3323px;width:1002px;border-top:1.5px solid #888}
.copyright{left:0;width:1200px;top:3338px;text-align:center;font-family:"Poppins",sans-serif;font-size:14.5px}
</style>
</head>
<body>
<div class="page">

  <!-- header -->
  <div class="abs brand"><span class="brand-dot"></span>Brightvale Crafts</div>
  <nav class="abs nav">
    <a class="active" href="#">Home</a><a href="#">About Us</a><a href="#">How It Works</a><a href="#">Services</a><a href="#">Blog</a>
  </nav>
  <div class="abs pill contact-btn">Contact Us</div>

  <!-- hero -->
  <div class="abs hero-art" role="img" aria-label="Hand holding a transparent glowing smartphone with app icons inside a blue and purple light ring"></div>
  <h1 class="abs heading hero-title">Welcome To Brightvale<br>Crafts</h1>
  <p class="abs hero-text">Lorem ipsum dolor sit amet, consectetur adipiscing elit, sed do eiusmod tempor incididunt ut labore et dolore magna aliqua.</p>
  <div class="abs pill hero-btn">Get Started</div>
  <div class="abs slider-nav" style="left:112px;border-color:#777"><svg width="10" height="14"><path d="M8 1 2 7l6 6" fill="none" stroke="#888" stroke-width="1.5"/></svg></div>
  <div class="abs slider-nav" style="left:154px"><svg width="10" height="14"><path d="M2 1l6 6-6 6" fill="none" stroke="#fff" stroke-width="1.8"/></svg></div>

  <!-- how it works -->
  <h2 class="abs heading section-title" style="top:744px">How It Works</h2>
  <p class="abs section-text" style="top:801px">Lorem ipsum dolor sit amet, consectetur adipiscing elit, sed do eiusmod tempor incididunt ut labore et dolore magna aliqua.<br>Ut enim ad minim veniam, quis nostrud exercitation ullamco laboris nisi ut aliquip ex ea commodo consequat.</p>
  <svg class="abs" style="left:0;top:890px" width="1200" height="150">
    <g fill="none" stroke-linecap="round" stroke-width="24">
      <path d="M133 30 A95 95 0 0 0 313 30" stroke="var(--red-dark)"/>
      <path d="M384 112 A95 95 0 0 1 564 112" stroke="var(--red-dark)"/>
      <path d="M636 30 A95 95 0 0 0 816 30" stroke="var(--red-mid)"/>
      <path d="M886 112 A95 95 0 0 1 1066 112" stroke="var(--red-dark)"/>
    </g>
    <g fill="none" stroke="#fff" stroke-width="2">
      <circle cx="223" cy="48" r="22"/><circle cx="223" cy="48" r="9"/>
      <rect x="448" y="60" width="52" height="34" rx="4"/><path d="M458 104h32M474 94v10"/>
      <circle cx="726" cy="36" r="12"/><path d="M700 70h52l-8 14h-36z"/>
      <circle cx="976" cy="96" r="20"/><path d="M966 118h20M968 126h16"/>
    </g>
    <path d="M80 92l-7 7 7 7" transform="translate(0,-8)" fill="none" stroke="#fff" stroke-width="2.4"/>
    <path d="M1121 92l7 7-7 7" transform="translate(0,-8)" fill="none" stroke="#fff" stroke-width="2.4"/>
  </svg>
  <div class="step-label" style="left:108px">Lorem ipsum</div>
  <div class="step-label" style="left:359px">Lorem ipsum</div>
  <div class="step-label active" style="left:611px">Lorem ipsum</div>
  <div class="step-label" style="left:861px">Lorem ipsum</div>

  <!-- about -->
  <div class="abs about-band"></div>
  <div class="abs about-photo" role="img" aria-label="Hand holding a smartphone showing a green security shield over lines of code"></div>
  <h2 class="abs heading about-title">About Us</h2>
  <p class="abs about-text">Lorem ipsum dolor sit amet, consectetur adipiscing elit, sed do eiusmod tempor incididunt ut labore et dolore magna aliqua. Ut enim ad minim veniam, quis nostrud exercitation ullamco laboris nisi ut aliquip ex ea commodo consequat. Duis aute irure dolor in reprehenderit in voluptate velit esse cillum dolore eu fugiat nulla pariatur. Excepteur sint occaecat cupidatat non proident, sunt in culpa qui officia deserunt mollit anim id est laborum.Sed ut perspiciatis unde omnis iste natus error sit voluptatem accusantium doloremque laudantium, totam rem aperiam, eaque ipsa quae ab illo inventore veritatis et quasi architecto beatae vitae dicta sunt explicabo.</p>
  <div class="abs pill about-btn">Read More</div>

  <!-- services -->
  <h2 class="abs heading section-title" style="top:1789px">Our Services</h2>
  <p class="abs section-text" style="top:1845px">Lorem ipsum dolor sit amet, consectetur adipiscing elit, sed do eiusmod tempor incididunt ut labore et dolore magna aliqua. Ut<br>enim ad minim veniam, quis nostrud exercitation ullamco laboris nisi ut aliquip ex ea commodo consequat.</p>

  <svg class="abs side-arrow" style="left:68px" width="20" height="20"><rect x="1" y="1" width="16" height="16" rx="4" fill="none" stroke="#bbb" stroke-width="1.3"/><path d="M5 9h8M10 6l3 3-3 3" fill="none" stroke="#bbb" stroke-width="1.3"/></svg>
  <svg class="abs side-arrow" style="left:1112px" width="20" height="20"><rect x="1" y="1" width="16" height="16" rx="4" fill="none" stroke="#ddd" stroke-width="1.5"/><path d="M13 9H5M8 6 5 9l3 3" fill="none" stroke="#ddd" stroke-width="1.5"/></svg>

  <div class="abs service" style="left:109px">
    <div class="service-icon"><svg width="52" height="52" fill="none" stroke="#222" stroke-width="2"><rect x="14" y="6" width="24" height="40" rx="4"/><circle cx="20" cy="18" r="6"/><path d="M30 28l4 4 6-8" stroke="var(--red)"/></svg></div>
    <h3>Lorem ipsum dolor</h3>
    <p>Sed ut perspiciatis unde omnis iste natus doloremque laudantium, totam rem aperiam, quasi architecto beatae vitae dicta sunt explicabo.</p>
    <svg class="go" width="24" height="24"><circle cx="12" cy="12" r="11" fill="#fff"/><path d="M10 7l5 5-5 5" fill="none" stroke="#000" stroke-width="2.4"/></svg>
  </div>
  <div class="abs service" style="left:444px">
    <div class="service-icon"><svg width="52" height="52" fill="none" stroke="#222" stroke-width="2"><rect x="10" y="6" width="26" height="40" rx="4"/><circle cx="23" cy="20" r="6"/><path d="M14 36c2-6 16-6 18 0"/><circle cx="40" cy="32" r="6" stroke="var(--red)"/></svg></div>
    <h3>Lorem ipsum dolor</h3>
    <p>Sed ut perspiciatis unde omnis iste natus doloremque laudantium, totam rem aperiam, quasi architecto beatae vitae dicta sunt explicabo.</p>
    <svg class="go" width="24" height="24"><circle cx="12" cy="12" r="11" fill="#fff"/><path d="M10 7l5 5-5 5" fill="none" stroke="#000" stroke-width="2.4"/></svg>
  </div>
  <div class="abs service" style="left:778px">
    <div class="service-icon"><svg width="52" height="52" fill="none" stroke="#222" stroke-width="2"><rect x="26" y="4" width="16" height="28" rx="3"/><rect x="6" y="34" width="24" height="12" rx="3"/><circle cx="13" cy="40" r="2"/><circle cx="23" cy="40" r="2"/></svg></div>
    <h3>Lorem ipsum dolor</h3>
    <p>Sed ut perspiciatis unde omnis iste natus doloremque laudantium, totam rem aperiam, quasi architecto beatae vitae dicta sunt explicabo.</p>
    <svg class="go" width="24" height="24"><circle cx="12" cy="12" r="11" fill="#fff"/><path d="M10 7l5 5-5 5" fill="none" stroke="#000" stroke-width="2.4"/></svg>
  </div>

  <!-- benefits -->
  <div class="abs benefits-band"></div>
  <h2 class="abs heading benefits-title">Brightvale Crafts Benefits:</h2>
  <ul class="abs benefits-list">
    <li><svg width="16" height="14"><path d="M1 7h12M8 2l5 5-5 5" fill="none" stroke="var(--red)" stroke-width="2.6"/></svg>Lorem ipsum dolor sit amet</li>
    <li><svg width="16" height="14"><path d="M1 7h12M8 2l5 5-5 5" fill="none" stroke="var(--red)" stroke-width="2.6"/></svg>Sed ut perspiciatis unde omnis iste natus error</li>
    <li><svg width="16" height="14"><path d="M1 7h12M8 2l5 5-5 5" fill="none" stroke="var(--red)" stroke-width="2.6"/></svg>Lorem ipsum dolor sit amet, consectetur adipiscing</li>
    <li><svg width="16" height="14"><path d="M1 7h12M8 2l5 5-5 5" fill="none" stroke="var(--red)" stroke-width="2.6"/></svg>Excepteur sint occaecat cupidatat non proident</li>
    <li><svg width="16" height="14"><path d="M1 7h12M8 2l5 5-5 5" fill="none" stroke="var(--red)" stroke-width="2.6"/></svg>Sed ut perspiciatis unde omnis iste natus</li>
    <li><svg width="16" height="14"><path d="M1 7h12M8 2l5 5-5 5" fill="none" stroke="var(--red)" stroke-width="2.6"/></svg>Quis autem vel eum iure reprehenderit qui</li>
  </ul>
  <div class="abs benefits-art" role="img" aria-label="Photo collage of hands using touch screens and digital interfaces in red and blue tones"></div>

  <!-- footer -->
  <h3 class="abs foot-title" style="left:112px">Quick Links</h3>
  <ul class="abs quick-links">
    <li><svg width="14" height="12"><path d="M1 6h11M7 1l5 5-5 5" fill="none" stroke="#fff" stroke-width="2.4"/></svg>Home</li>
    <li><svg width="14" height="12"><path d="M1 6h11M7 1l5 5-5 5" fill="none" stroke="#fff" stroke-width="2.4"/></svg>About Us</li>
    <li><svg width="14" height="12"><path d="M1 6h11M7 1l5 5-5 5" fill="none" stroke="#fff" stroke-width="2.4"/></svg>Services</li>
    <li><svg width="14" height="12"><path d="M1 6h11M7 1l5 5-5 5" fill="none" stroke="#fff" stroke-width="2.4"/></svg>Blog</li>
    <li><svg width="14" height="12"><path d="M1 6h11M7 1l5 5-5 5" fill="none" stroke="#fff" stroke-width="2.4"/></svg>Contact Us</li>
  </ul>
  <div class="abs socials" aria-label="Social media links">
    <span class="social"></span><span class="social"></span><span class="social"></span><span class="social"></span>
  </div>
  <div class="abs vrule" style="left:315px"></div>

  <h3 class="abs foot-title" style="left:369px">Contact Details</h3>
  <div class="abs detail" style="top:3017px">
    <span class="detail-icon"><svg width="16" height="16"><path d="M4 2l3 3-2 2c1 2 2 3 4 4l2-2 3 3-2 2C7 14 2 9 2 4z" fill="#fff"/></svg></span>
    <span class="detail-label" style="top:-2px">Phone;</span>
    <span class="detail-value" style="top:23px">+1 555 0142 7788</span>
  </div>
  <div class="abs dots" style="top:3079px"></div>
  <div class="abs detail" style="top:3099px">
    <span class="detail-icon"><svg width="16" height="12"><rect x="1" y="1" width="14" height="10" fill="#fff"/><path d="M1 1l7 6 7-6" fill="none" stroke="#000" stroke-width="1.2"/></svg></span>
    <span class="detail-label" style="top:-2px">Email:</span>
    <span class="detail-value" style="top:23px">info@brightvalecrafts.au</span>
  </div>
  <div class="abs dots" style="top:3161px"></div>
  <div class="abs detail" style="top:3183px">
    <span class="detail-icon"><svg width="16" height="16"><path d="M4 2l3 3-2 2c1 2 2 3 4 4l2-2 3 3-2 2C7 14 2 9 2 4z" fill="#fff"/></svg></span>
    <span class="detail-label" style="top:-2px">Address:</span>
    <span class="detail-value" style="top:23px">Brightvale Crafts,<br>Northbank, Australia.</span>
  </div>
  <div class="abs vrule" style="left:684px"></div>

  <h3 class="abs foot-title" style="left:730px">Contact Me</h3>
  <div class="abs field" style="top:3012px">Name:</div>
  <div class="abs field" style="top:3065px">Email:</div>
  <div class="abs field" style="top:3117px">Address:</div>
  <div class="abs submit">Submit Now</div>

  <div class="abs bottom-rule"></div>
  <p class="abs copyright">Copyrights@2023.Brightvale Crafts.All Rights Reserved</p>
</div>
</body>
</html>
```